CBD AgriBusiness Verdant Laurel Business Card

We are HiTec producer of medical cannabis CBD Switzerland of high quality. Our website is morvelta.com, we will also revisit it graphically, the winner of this contest will be the graphic designer chosen for the new design of the website. We stand out by the skill of the team, many of our engineers we win laurel verdant. I join the current map to take as an example but to revisit completely: deletion of surname and first name, modification of funds (front / back), reorganization of text info, highlighting the address of the website. three characteristics define the business card: Professional, Class, refined. The business card must be optimized for soft-touch and selective varnish printing.
Updates

Besoin de plus de jours pour examiner

Target Market(s)

Customers and Suppliers

Industry/Entity Type

Agribusiness

Contact Information for Business Card

Logo, Tél / Whatsapp, mail, url du site : morvelta.com

Font styles to use
Sans Serif

Requirements
Must have
• Logo of morvelta.com
Nice to have
• a design that stands out well on the selective varnish
Should not have
• Last name and first name

```html
<!DOCTYPE html>
<html lang="en">
<head>
<meta charset="utf-8">
<title>Verdant Laurel Business Card</title>
<link rel="stylesheet" href="https://fonts.googleapis.com/css2?family=Montserrat:wght@700&family=Lato:wght@400&display=swap">
<style>
  :root {
    --stage: #1f1f1f;
    --card-light: #ffffff;
    --brand-green: #9cc96c;
    --ink: #1e1e1e;
    --white: #ffffff;
    --shadow: rgba(0, 0, 0, 0.55);
  }
  html, body {
    margin: 0;
    padding: 0;
    width: 1200px;
    height: 900px;
    overflow: hidden;
    background: var(--stage);
  }
  .stage {
    position: relative;
    width: 1200px;
    height: 900px;
  }
  .card {
    position: absolute;
    top: 275px;
    width: 477px;
    height: 294px;
    box-shadow: 3px 4px 6px var(--shadow);
  }
  .card--front {
    left: 120px;
    background: var(--card-light);
    border-radius: 0 56px 0 56px;
  }
  .card--back {
    left: 619px;
    top: 276px;
    height: 293px;
    background: var(--brand-green);
    border-radius: 56px 0 56px 0;
  }
  .wordmark {
    position: absolute;
    display: flex;
    align-items: center;
    gap: 14px;
    font-family: "Montserrat", sans-serif;
    font-weight: 700;
    letter-spacing: 0.5px;
    line-height: 1;
    white-space: nowrap;
  }
  .wordmark__square {
    display: block;
    width: 30px;
    height: 30px;
  }
  .card--front .wordmark {
    left: 94px;
    top: 86px;
    font-size: 54px;
    color: var(--brand-green);
  }
  .card--front .wordmark__square { background: var(--brand-green); }
  .card--back .wordmark {
    left: 86px;
    top: 126px;
    font-size: 46px;
    color: var(--white);
  }
  .card--back .wordmark__square {
    background: var(--white);
    width: 26px;
    height: 26px;
  }
  .contact-list {
    position: absolute;
    left: 154px;
    top: 195px;
    margin: 0;
    padding: 0;
    list-style: none;
    font-family: "Lato", sans-serif;
    font-size: 15px;
    color: var(--ink);
  }
  .contact-list li {
    display: flex;
    align-items: center;
    gap: 5px;
    height: 24px;
  }
  .contact-list svg {
    width: 14px;
    height: 14px;
    fill: var(--brand-green);
    flex: none;
  }
</style>
</head>
<body>
<main class="stage">
  <section class="card card--front" aria-label="Card front">
    <div class="wordmark"><span class="wordmark__square"></span>morvelta</div>
    <ul class="contact-list">
      <li>
        <svg viewBox="0 0 16 16" aria-hidden="true"><circle cx="8" cy="8" r="8"/><path d="M5.2 3.8l1.5-.3.9 2.2-1 .8c.5 1.1 1.3 1.9 2.4 2.4l.8-1 2.2.9-.3 1.5c-3.4.2-6.7-3.1-6.5-6.5z" fill="#fff"/></svg>
        +41 79 555 01 42
      </li>
      <li>
        <svg viewBox="0 0 16 16" aria-hidden="true"><rect x="1" y="3" width="14" height="10"/><path d="M1.5 3.5L8 9l6.5-5.5" fill="none" stroke="#fff" stroke-width="1.3"/></svg>
        office@morvelta.com
      </li>
      <li>
        <svg viewBox="0 0 16 16" aria-hidden="true"><circle cx="8" cy="8" r="7.5"/><path d="M4 5c1.5-.5 2.5.5 2.3 1.8-.2 1-1.4 1.2-1.2 2.4.1.8.8 1.3.6 2.6M10 3c-.4 1 .3 1.7 1.3 1.8 1 .1 1.5.9 1.2 2" fill="none" stroke="#fff" stroke-width="1.1"/></svg>
        www.morvelta.com
      </li>
    </ul>
  </section>
  <section class="card card--back" aria-label="Card back">
    <div class="wordmark"><span class="wordmark__square"></span>morvelta</div>
  </section>
</main>
</body>
</html>
```